Copperleaf Motorized Shade Business Card

Hello, we've had our logo made. Now we are looking for a clean and cool looking business card. One side can just be the logo with any design elements that might look good with it. The other side will be Name, Phone Number and Email. There will not be an address on the card.

```html
<!DOCTYPE html>
<html lang="en">
<head>
<meta charset="utf-8">
<title>Copperleaf Motorized Shade – Business Card</title>
<link href="https://fonts.googleapis.com/css2?family=Montserrat:wght@400;500;700;800&display=swap" rel="stylesheet">
<style>
  :root {
    --page: #f2f3f5;
    --navy: #093d73;
    --navy-light: #0f4a85;
    --yellow: #fdc10e;
    --white: #ffffff;
    --faint: rgba(255, 255, 255, 0.22);
  }
  * { box-sizing: border-box; margin: 0; padding: 0; }
  html, body {
    width: 1200px; height: 1200px; overflow: hidden;
    background: var(--page);
    font-family: "Montserrat", sans-serif;
  }
  .canvas { position: relative; width: 1200px; height: 1200px; }

  .card {
    position: absolute; left: 195px; width: 813px; height: 462px;
    border-radius: 40px; overflow: hidden;
  }
  .card-front { top: 87px; background: var(--white); border: 1px solid #e2e5ea; }
  .card-back { top: 638px; background: var(--navy); }

  /* front */
  .brand {
    position: absolute; left: 0; right: 0; top: 150px;
    display: flex; align-items: center; justify-content: center; gap: 22px;
  }
  .brand-square { width: 58px; height: 58px; background: var(--yellow); }
  .brand-name {
    color: var(--navy); font-weight: 800; font-size: 44px; line-height: 1.05;
    letter-spacing: 1px; text-transform: uppercase; width: 430px;
  }

  /* back */
  .back-band {
    position: absolute; left: 0; bottom: 0; width: 100%; height: 150px;
    background: var(--navy-light);
  }
  .brand-faint {
    position: absolute; left: 64px; top: 160px; width: 220px;
    color: var(--faint); font-weight: 800; font-size: 28px; line-height: 1.1;
    text-transform: uppercase; letter-spacing: 1px;
  }
  .timeline { position: absolute; left: 0; top: 0; }
  .person-name {
    position: absolute; left: 356px; top: 110px;
    color: var(--white); font-weight: 700; font-size: 22px; letter-spacing: .5px;
  }
  .person-role {
    position: absolute; left: 356px; top: 138px;
    color: var(--yellow); font-size: 12px; font-weight: 500;
  }
  .contact {
    position: absolute; left: 380px; color: var(--white);
    font-size: 15px; font-weight: 400; letter-spacing: .3px; line-height: 1.35;
  }
  .contact-phone { top: 183px; }
  .contact-email { top: 234px; }
  .contact-web { top: 286px; }
</style>
</head>
<body>
<main class="canvas">
  <section class="card card-front">
    <div class="brand">
      <span class="brand-square"></span>
      <span class="brand-name">Copperleaf Motorized Shade</span>
    </div>
  </section>

  <section class="card card-back">
    <div class="back-band"></div>
    <div class="brand-faint">Copperleaf Motorized Shade</div>

    <svg class="timeline" width="813" height="462" viewBox="0 0 813 462">
      <polyline points="304,103 330,150 330,192 318,218 330,243 318,270 330,295 304,340"
        fill="none" stroke="#fdc10e" stroke-width="2"/>
      <circle cx="304" cy="103" r="7" fill="#fdc10e"/>
      <circle cx="304" cy="340" r="7" fill="#fdc10e"/>
      <g fill="#fdc10e">
        <circle cx="330" cy="192" r="15"/>
        <circle cx="330" cy="243" r="15"/>
        <circle cx="330" cy="295" r="15"/>
      </g>
      <!-- phone -->
      <path d="M324 185 l4 0 l2 5 l-2 2 q2 4 6 6 l2 -2 l5 2 l0 4 q-10 1 -17 -17 z" fill="#093d73"/>
      <!-- email -->
      <rect x="322" y="237" width="16" height="12" rx="1" fill="#093d73"/>
      <polyline points="322,238 330,244 338,238" fill="none" stroke="#fdc10e" stroke-width="1.5"/>
      <!-- web -->
      <circle cx="330" cy="295" r="8" fill="none" stroke="#093d73" stroke-width="2"/>
      <ellipse cx="330" cy="295" rx="3.5" ry="8" fill="none" stroke="#093d73" stroke-width="1.5"/>
      <line x1="322" y1="295" x2="338" y2="295" stroke="#093d73" stroke-width="1.5"/>
    </svg>

    <div class="person-name">DANA WHITFIELD</div>
    <div class="person-role">Solution Manager</div>
    <div class="contact contact-phone">+012 345 6789 / +012 345 6789</div>
    <div class="contact contact-email">urname@email.com</div>
    <div class="contact contact-web">urwebsitename.com</div>
  </section>
</main>
</body>
</html>
```